Ridgeway Framers Business Card

I'm looking for a business card design for a start-up Handyman/Construction Company. The organization will double as a ministry to the homeless, hoping to create job opportunity and training to the homeless, providing a pathway back to being "homed". I'm looking for a simple to "seeming" simple design. Open to all thoughts.

Industry/Entity Type

Ministry

Requirements
Must have
• Logo (Attached), Name, Phone, Email and Address. Note - "*Registered and Insured".

```html
<!DOCTYPE html>
<html lang="en">
<head>
<meta charset="utf-8">
<title>Ridgeway Framers Business Card</title>
<link rel="stylesheet" href="https://fonts.googleapis.com/css2?family=Delius&display=swap">
<style>
  :root {
    --page-bg: #e9ecec;
    --card-light: #f7f7f6;
    --card-mid: #e6e6e4;
    --ink-navy: #1f3157;
    --shadow: rgba(0, 0, 0, 0.18);
  }
  * { margin: 0; padding: 0; box-sizing: border-box; }
  html, body {
    width: 1200px;
    height: 1000px;
    overflow: hidden;
    background: var(--page-bg);
    font-family: "Delius", cursive, sans-serif;
    color: var(--ink-navy);
  }
  .canvas {
    position: relative;
    width: 1200px;
    height: 1000px;
  }
  .card {
    position: absolute;
    left: 215px;
    width: 770px;
    height: 440px;
    background: linear-gradient(160deg, var(--card-light) 0%, var(--card-mid) 100%);
    box-shadow: 0 6px 18px var(--shadow);
  }
  .card--front { top: 40px; }
  .card--back { top: 520px; }

  .brand-name {
    position: absolute;
    font-size: 58px;
    font-weight: 400;
    letter-spacing: 1px;
    line-height: 1;
    color: var(--ink-navy);
    white-space: nowrap;
  }
  .card--front .brand-name { left: 62px; top: 62px; }
  .card--back .brand-name { right: 70px; top: 150px; }

  .holder-name {
    position: absolute;
    left: 62px;
    top: 240px;
    font-size: 27px;
  }
  .contact {
    position: absolute;
    right: 66px;
    bottom: 40px;
    text-align: right;
    font-size: 21px;
    line-height: 27px;
    font-style: normal;
  }
</style>
</head>
<body>
<main class="canvas">
  <section class="card card--front" aria-label="Card front">
    <div class="brand-name">Ridgeway Framers</div>
    <p class="holder-name">Dale Mercer</p>
    <address class="contact">
      PO Box 482107<br>
      Danville, KY 40422<br>
      (859) 555-0172<br>
      dale.rwf@example.com<br>
      Registered and Insured
    </address>
  </section>

  <section class="card card--back" aria-label="Card back">
    <div class="brand-name">Ridgeway Framers</div>
  </section>
</main>
</body>
</html>
```